Design a label for a dog shampoo names furbloom, the sell point of this series of shampoo is “just like wash your dogs with milk, not harm for your hand ”, the style could be gentle or professional or even amazing.

Use only 2 colors in the design job, the color of our logo could be changed, it depends on your whole page. Please design in CDR or ai.

update:
Pls do more change with the fonts when you design the front page, including title and details. Try more styles of fonts. Addition, this design will be printed on the bottle, no a label stick on it.
Updates

Do not put a real dog or animal on the page, Pay more attention to the types of fonts

Reason: Expect for more design idea.

Target Market(s)

people 20-30 years old who have dogs and cats at home

Industry/Entity Type

It Professional

Requirements
Nice to have
• It would be nice if you add some detail words in the design of the right side.

```html
<!DOCTYPE html>
<html lang="en">
<head>
<meta charset="utf-8">
<title>furbloom Shampoo – Label Options</title>
<link rel="stylesheet" href="https://fonts.googleapis.com/css2?family=Archivo+Black&family=Comfortaa:wght@400;700&family=Mouse+Memoirs&family=Quicksand:wght@500;600&family=Roboto+Condensed:wght@700&display=swap">
<style>
  :root {
    --teal: #12acd0;
    --pink: #e5158c;
    --ink: #111111;
    --paper: #ffffff;
    --rule: #8a8a8a;
    --foam-light: #eef8fb;
    --foam-mid: #cfe9f2;
    --foam-deep: #a9d6e6;
  }
  * { box-sizing: border-box; margin: 0; padding: 0; }
  html, body { width: 1200px; height: 767px; overflow: hidden; background: var(--paper); }

  .label-sheet {
    position: relative;
    width: 1200px;
    height: 767px;
    display: flex;
    background: var(--paper);
  }
  .label {
    position: relative;
    height: 100%;
    border: 1px solid var(--rule);
    overflow: hidden;
    text-align: center;
  }
  .label--bold { width: 396px; }
  .label--soft { width: 401px; border-left: none; }
  .label--playful { width: 403px; border-left: none; }

  .brand {
    position: absolute;
    top: 62px;
    left: 0; right: 0;
    display: flex;
    justify-content: center;
    align-items: center;
    gap: 10px;
  }
  .brand__name {
    font-family: "Comfortaa", sans-serif;
    font-weight: 700;
    font-size: 44px;
    color: var(--teal);
    line-height: 1;
  }
  .brand__dot {
    width: 16px; height: 16px;
    border-radius: 50%;
    background: var(--teal);
  }

  .tagline, .product, .benefit, .claim, .volume {
    position: absolute;
    left: 0; right: 0;
    white-space: nowrap;
  }
  .tagline { top: 190px; font-size: 21px; line-height: 1; }
  .product { top: 228px; line-height: 1; }
  .benefit { top: 324px; font-size: 19px; line-height: 26px; }
  .claim { top: 470px; font-size: 20px; line-height: 26px; z-index: 2; }
  .volume {
    bottom: 10px;
    font-family: "Archivo Black", sans-serif;
    font-size: 16px;
    color: var(--ink);
    z-index: 2;
  }

  .foam-art {
    position: absolute;
    left: 0; right: 0;
    top: 405px; bottom: 0;
    background:
      radial-gradient(ellipse at 30% 70%, rgba(20,20,20,0.55) 0 14%, transparent 15%),
      radial-gradient(ellipse at 75% 72%, rgba(20,20,20,0.45) 0 11%, transparent 12%),
      linear-gradient(to bottom, var(--paper) 0%, var(--foam-light) 35%, var(--foam-mid) 75%, var(--foam-deep) 100%);
    z-index: 1;
  }

  /* Option 1 – heavy grotesque */
  .label--bold .tagline { font-family: "Roboto Condensed", sans-serif; font-weight: 700; color: var(--teal); }
  .label--bold .product { font-family: "Archivo Black", sans-serif; font-size: 62px; color: var(--pink); letter-spacing: -1px; top: 234px; }
  .label--bold .benefit { font-family: "Archivo Black", sans-serif; font-size: 18px; color: var(--teal); }
  .label--bold .claim { font-family: "Roboto Condensed", sans-serif; font-weight: 700; color: var(--pink); }

  /* Option 2 – light rounded */
  .label--soft .tagline { font-family: "Quicksand", sans-serif; font-weight: 600; font-size: 22px; color: var(--pink); }
  .label--soft .product { font-family: "Comfortaa", sans-serif; font-weight: 400; font-size: 62px; color: var(--teal); top: 236px; }
  .label--soft .benefit { font-family: "Quicksand", sans-serif; font-weight: 500; font-size: 21px; color: var(--pink); }
  .label--soft .claim { font-family: "Quicksand", sans-serif; font-weight: 500; color: var(--teal); }

  /* Option 3 – playful tall */
  .label--playful .tagline { font-family: "Roboto Condensed", sans-serif; font-weight: 700; font-size: 22px; color: var(--ink); }
  .label--playful .product { font-family: "Mouse Memoirs", sans-serif; font-size: 124px; color: var(--pink); top: 210px; letter-spacing: 2px; }
  .label--playful .benefit { font-family: "Archivo Black", sans-serif; font-size: 18px; color: var(--ink); top: 330px; }
  .label--playful .claim { font-family: "Roboto Condensed", sans-serif; font-weight: 700; color: var(--pink); }
</style>
</head>
<body>
<main class="label-sheet">

  <section class="label label--bold">
    <div class="brand"><span class="brand__name">furbloom</span><span class="brand__dot"></span></div>
    <p class="tagline">SUPER-CONDITIONING &amp; NUTRIENT</p>
    <h1 class="product">SHAMPOO</h1>
    <p class="benefit">MOISTURE-RICH, SMOOTH<br>AND SILKY</p>
    <p class="claim">wash your dogs just like with milk<br>not harm for your hand</p>
    <div class="foam-art" role="img" aria-label="Soap bubbles rising around two black paw prints"></div>
    <p class="volume">1000 ML</p>
  </section>

  <section class="label label--soft">
    <div class="brand"><span class="brand__name">furbloom</span><span class="brand__dot"></span></div>
    <p class="tagline">SUPER-CONDITIONING &amp; NUTRIENT</p>
    <h1 class="product">SHAMPOO</h1>
    <p class="benefit">MOISTURE-RICH, SMOOTH<br>AND SILKY</p>
    <p class="claim">wash your dogs just like with milk<br>not harm for your hand</p>
    <div class="foam-art" role="img" aria-label="Soap bubbles rising around two black paw prints"></div>
    <p class="volume">1000 ML</p>
  </section>

  <section class="label label--playful">
    <div class="brand"><span class="brand__name">furbloom</span><span class="brand__dot"></span></div>
    <p class="tagline">SUPER-CONDITIONING &amp; NUTRIENT</p>
    <h1 class="product">SHAMPOO</h1>
    <p class="benefit">MOISTURE-RICH, SMOOTH<br>AND SILKY</p>
    <p class="claim">wash your dogs just like with milk<br>not harm for your hand</p>
    <div class="foam-art" role="img" aria-label="Soap bubbles rising around two black paw prints"></div>
    <p class="volume">1000 ML</p>
  </section>

</main>
</body>
</html>
```